Design a flyer

Hi, I need a flyer designed for an electrical and air conditioning company based in brisbane, Australia.
We service the domestic market.
Flyer is to be double sided
Flyer size DL 210mm X 99mm
Was thinking one side services and discount coupons and the other side possible testimonials.
I have logo uploaded followed with the vehicle advertising, advertising stand alone sign and also business cards.
--------------------------
Coupon Cut out
save $150 OFF switchboard upgrades
save $150 Complimentary Electrical safety inspection
save $50 OFF Air Conditioner install or Service
save $50 next job if you leave feedback for first job
OVER $400 WORTH OF SAVINGS!
Our promise to you
* we will Arrive on time or we will pay you $100
* Before any job begins you will know the exact price
* We will leave your place as clean as we arrived
* if there is a problem and its our fault we will fix it for free
* provide a 12 month warranty on all parts
* we will provide friendly helpful service and advice
Phone number is 0487 625 903
Company Name - Tavolinex
License: 58164
ABN - 61 208 395 172
Also add vornel pay, zund and paklin logo at the bottom
----------------------------
Here is what some of my customers have had to say
Extremely professional...
“Arrived when he said he would, sent through a written quote and was very reasonable. He also checked out our smoke
detectors whist he was here. He installed 2 ceiling fans and an air conditioner. He
cleaned up the mess and was very efficient. I will definitely use him again and recommend
him to family and friends”
R.M – Stretton
“Excellent service provider. He arrived on time with a call before arriving, than carried all jobs quickly and efficiently and left no mess at all. I will definitely recommend his service to others requiring an electrician. Thanks again!”
K.S – Greenslopes
“Over the long weekend, I had problems with my power, not only did you pick up the first phone call but you came out at 5am to fix it. Love the fact you’re a 24hr service!”
T.W – Mount Gravatt
---------------------------
NEW changes
Hi everyone,
Just want to say well done all the designers look great!
I will soon be choosing a winner, but there are a couple of changes i would like to make, if you revise you will be in for a win.
Instead of Save 50 if you leave feedback for the first job quote. I want to change that put $110 cross out and put $71.50 Install & Supply LED Downlights (min 20)
I want this to be the number one followed by switch board upgrade cut out.
Also $50 off air con install - don't put service.
And the third testimonial T.W Make sure it has a full stop
Also keep in mind. It is an electrical & air conditioning company.
Be creative with your design, don't want to see any pictures of people as they are not working for us at this time.
Remember key focus, on coupons, phone numbers, and website. zund and vornelpay can be small and out of the way same with the license numbers.
Thank you
Good Luck!
Target Market(s)
Domestic Market - Home owners
Industry/Entity Type
Air Conditioning

```html
<!DOCTYPE html>
<html lang="en">
<head>
<meta charset="utf-8">
<title>Tavolinex – Electrical &amp; Air Conditioning Flyer</title>
<link href="https://fonts.googleapis.com/css2?family=Arimo:wght@400;700&family=Barlow:wght@400;500;600&family=Questrial&display=swap" rel="stylesheet">
<style>
  :root{
    --blue:#1f76c0;
    --blue-dark:#175f9e;
    --orange:#e4692b;
    --ink:#333a40;
    --ink-soft:#4a4f55;
    --paper-1:#f3f4f5;
    --paper-2:#dfe1e3;
    --backdrop:#d4d5d6;
    --bullet:#a9c3ee;
  }
  *{box-sizing:border-box;margin:0;padding:0}
  html,body{width:1200px;height:2232px;overflow:hidden}
  body{background:var(--backdrop);position:relative;font-family:"Arimo",Arial,sans-serif}
  .flyer{
    position:absolute;left:85px;top:25px;width:1030px;height:2182px;overflow:hidden;
    background:linear-gradient(180deg,var(--paper-1) 0%,var(--paper-2) 45%,var(--paper-1) 70%,var(--paper-2) 100%);
  }
  .abs{position:absolute}

  /* brand */
  .brand-name{left:0;width:1030px;top:130px;text-align:center;font-family:"Barlow",sans-serif;font-weight:400;font-size:140px;line-height:1;color:var(--blue);letter-spacing:4px}
  .rule{left:40px;width:946px;height:3px;background:var(--orange)}
  .rule::before,.rule::after{content:"";position:absolute;top:-3px;width:9px;height:9px;border-radius:50%;background:var(--blue)}
  .rule::before{left:-4px}.rule::after{right:-4px}
  .rule-top{top:332px}.rule-bottom{top:412px}
  .service-title{left:0;width:1030px;top:348px;text-align:center;font-family:"Barlow",sans-serif;font-weight:500;font-size:43px;line-height:1.2;color:var(--ink);letter-spacing:1px}

  /* ribbon */
  .ribbon{left:0;top:0}
  .ribbon-text{left:0;width:1030px;color:#fff;font-family:"Arimo",sans-serif;font-weight:700;font-size:38px;line-height:1.1;display:flex;justify-content:center;gap:36px}
  .ribbon-text span::before{content:"";display:inline-block;width:15px;height:15px;border-radius:50%;background:var(--bullet);margin-right:6px;vertical-align:4px}
  .ribbon-row-1{top:438px}.ribbon-row-2{top:496px}

  /* promise */
  .promise-tag{left:0;top:0}
  .promise-title{left:100px;top:595px;color:#fff;font-weight:700;font-size:46px;line-height:1.2;font-family:"Arimo",sans-serif}
  .promise-list{left:62px;top:683px;list-style:none}
  .promise-list li{height:65.8px;display:flex;align-items:center;font-family:"Questrial",sans-serif;font-size:35px;color:var(--ink)}
  .promise-list svg{width:28px;height:28px;margin-right:10px;flex:none}

  /* coupons */
  .coupon{left:0;width:1030px;display:flex;flex-direction:column;align-items:center;justify-content:center;color:#fff;font-weight:700;font-size:50px;line-height:1.22;text-align:center}
  .coupon .amount{font-size:68px}
  .coupon-orange{background:var(--orange)}
  .coupon-blue{background:var(--blue)}
  .coupon-1{top:1082px;height:174px}
  .coupon-2{top:1262px;height:172px}
  .coupon-3{top:1440px;height:171px}
  .coupon-4{top:1617px;height:170px}
  .cut{left:0;width:1030px;height:0;border-top:3px dashed #b9bcbf}
  .bolt{width:52px;height:86px;top:50%;margin-top:-43px}
  .bolt-left{left:54px}.bolt-right{right:54px}

  /* footer */
  .payments{left:62px;top:1836px;display:flex;gap:24px;align-items:center}
  .pay{font-family:"Arimo",sans-serif;font-weight:700;font-size:36px;color:var(--blue-dark);display:flex;align-items:center;gap:8px}
  .pay i{display:inline-block;width:16px;height:16px;background:var(--orange)}
  .licence{right:76px;top:1815px;text-align:right;font-weight:700;font-size:32px;line-height:1.7;color:var(--ink-soft)}
  .contact-band{left:0;top:1926px}
  .phone{left:86px;top:1930px;height:136px;display:flex;align-items:center;gap:18px;color:#fff;font-weight:700;font-size:114px;letter-spacing:1px;text-shadow:4px 4px 0 #2b2b2b}
  .phone svg{width:108px;height:108px;flex:none;filter:drop-shadow(3px 3px 0 #2b2b2b)}
  .website{left:0;width:1030px;top:2066px;height:116px;display:flex;align-items:center;justify-content:center;gap:12px;color:#fff;font-weight:700;font-size:68px;text-shadow:3px 3px 0 #2b2b2b}
  .website svg{width:50px;height:50px;flex:none;filter:drop-shadow(2px 2px 0 #2b2b2b)}
</style>
</head>
<body>
<svg width="0" height="0" style="position:absolute" aria-hidden="true">
  <defs>
    <symbol id="bolt" viewBox="0 0 52 86">
      <polygon points="30,0 52,8 44,10 28,40 42,38 8,86 18,50 4,52 30,8 22,4"/>
    </symbol>
    <symbol id="tick" viewBox="0 0 24 24">
      <rect x="2" y="5" width="17" height="17" fill="#fff" stroke="#6a6e72" stroke-width="1.5"/>
      <path d="M5 12 L10 18 L22 3" fill="none" stroke="var(--orange)" stroke-width="3.2" stroke-linecap="round" stroke-linejoin="round"/>
    </symbol>
  </defs>
</svg>

<main class="flyer">
  <header>
    <h1 class="abs brand-name">Tavolinex</h1>
    <div class="abs rule rule-top"></div>
    <h2 class="abs service-title">ELECTRICAL &amp; AIR CONDITIONING SERVICES</h2>
    <div class="abs rule rule-bottom"></div>
  </header>

  <svg class="abs ribbon" width="1030" height="600" aria-hidden="true">
    <polygon points="40,422 991,422 929,528 885,514 876,558 155,558 146,514 102,528" fill="var(--blue)"/>
    <polygon points="155,514 146,514 155,558" fill="var(--blue-dark)"/>
    <polygon points="876,514 885,514 876,558" fill="var(--blue-dark)"/>
  </svg>
  <div class="abs ribbon-text ribbon-row-1"><span>Domestic</span><span>Commercial</span></div>
  <div class="abs ribbon-text ribbon-row-2"><span>Install</span><span>Service</span><span>Maintenance</span></div>

  <section>
    <svg class="abs promise-tag" width="700" height="700" aria-hidden="true">
      <polygon points="42,591 578,591 613,656 62,656 52,624" fill="var(--orange)"/>
    </svg>
    <h3 class="abs promise-title">Our promise to you</h3>
    <ul class="abs promise-list">
      <li><svg><use href="#tick"/></svg>We will Arrive on time or we will pay you $100</li>
      <li><svg><use href="#tick"/></svg>Before any job begins you will know the exact price</li>
      <li><svg><use href="#tick"/></svg>We will leave your place as clean as we arrived</li>
      <li><svg><use href="#tick"/></svg>If there is a problem and its our fault we will fix it for free</li>
      <li><svg><use href="#tick"/></svg>Provide a 12 month warranty on all parts</li>
      <li><svg><use href="#tick"/></svg>We will provide friendly helpful service and advice</li>
    </ul>
  </section>

  <section>
    <div class="abs coupon coupon-orange coupon-1">
      <svg class="abs bolt bolt-left" fill="var(--blue)"><use href="#bolt"/></svg>
      <div>Save <span class="amount">$150</span> OFF</div>
      <div>switchboard upgrades</div>
      <svg class="abs bolt bolt-right" fill="var(--blue)"><use href="#bolt"/></svg>
    </div>
    <div class="abs cut" style="top:1257px"></div>
    <div class="abs coupon coupon-blue coupon-2">
      <svg class="abs bolt bolt-left" fill="var(--orange)"><use href="#bolt"/></svg>
      <div>Save <span class="amount">$150</span> Complimentary</div>
      <div>Electrical safety inspection</div>
      <svg class="abs bolt bolt-right" fill="var(--orange)"><use href="#bolt"/></svg>
    </div>
    <div class="abs cut" style="top:1435px"></div>
    <div class="abs coupon coupon-orange coupon-3">
      <svg class="abs bolt bolt-left" fill="var(--blue)"><use href="#bolt"/></svg>
      <div>Save <span class="amount">$50</span> OFF Air Conditioner</div>
      <div>install or Service</div>
      <svg class="abs bolt bolt-right" fill="var(--blue)"><use href="#bolt"/></svg>
    </div>
    <div class="abs cut" style="top:1612px"></div>
    <div class="abs coupon coupon-blue coupon-4">
      <svg class="abs bolt bolt-left" fill="var(--orange)"><use href="#bolt"/></svg>
      <div>Save <span class="amount">$50</span> next job if you</div>
      <div>leave feedback for first job</div>
      <svg class="abs bolt bolt-right" fill="var(--orange)"><use href="#bolt"/></svg>
    </div>
    <div class="abs cut" style="top:1788px"></div>
  </section>

  <footer>
    <div class="abs payments">
      <span class="pay">zund</span>
      <span class="pay">vornelpay</span>
      <span class="pay"><i></i>paklin</span>
    </div>
    <div class="abs licence">License: 58164<br>ABN - 61 208 395 172</div>

    <svg class="abs contact-band" width="1030" height="256" aria-hidden="true">
      <rect x="0" y="0" width="1030" height="256" fill="var(--blue)"/>
      <polygon points="0,0 1030,0 1030,140 102,140 0,22" fill="var(--orange)"/>
    </svg>
    <div class="abs phone">
      <svg viewBox="0 0 100 100" aria-hidden="true">
        <circle cx="50" cy="50" r="45" fill="none" stroke="#fff" stroke-width="6"/>
        <path d="M36 24 L46 38 L40 46 C44 56 50 62 58 66 L66 60 L78 70 L70 80 C48 80 24 56 24 34 Z" fill="#fff"/>
      </svg>
      <span>0487 625 903</span>
    </div>
    <div class="abs website">
      <svg viewBox="0 0 40 40" aria-hidden="true">
        <circle cx="20" cy="20" r="17" fill="none" stroke="#fff" stroke-width="3"/>
        <ellipse cx="20" cy="20" rx="7" ry="17" fill="none" stroke="#fff" stroke-width="2.5"/>
        <line x1="3" y1="20" x2="37" y2="20" stroke="#fff" stroke-width="2.5"/>
        <line x1="7" y1="11" x2="33" y2="11" stroke="#fff" stroke-width="2"/>
        <line x1="7" y1="29" x2="33" y2="29" stroke="#fff" stroke-width="2"/>
      </svg>
      <span>www.Tavolinex.com.au</span>
    </div>
  </footer>
</main>
</body>
</html>
```